Business card for Northland's Blue Wagon.

Good day i am looking for a business card design for my business.
The name of the business is Northland's Blue Wagon. It is a van rental business that provides a driver and helper to the customer. Customer have use to van for small moves, studio or 1 bedroom, Moving furniture like couch or kitchen cabinets.
We are available evenings, weekends and holidays.
the means to contact us is by phone at 628-947-2071; By emails at Oakridge@northlandsbluewagon.net; or by social media, Facebook and Instagram.
You can see attached pictures of the van and or logo.

```html
<!DOCTYPE html>
<html lang="en">
<head>
<meta charset="UTF-8">
<title>Northland's Blue Wagon — Business Card</title>
<link rel="stylesheet" href="https://fonts.googleapis.com/css2?family=Arimo:wght@400;700&display=swap">
<style>
  :root {
    --brand-red: #d10000;
    --ink: #1a1a1a;
    --muted: #8a8a8a;
    --paper: #ffffff;
    --rule: #d6d6d6;
    --ghost: #f7efe6;
    --stage: #3a3a3a;
  }
  * { margin: 0; padding: 0; box-sizing: border-box; }
  html, body { width: 1200px; height: 689px; overflow: hidden; }
  body {
    background: var(--stage);
    font-family: "Arimo", Arial, sans-serif;
    position: relative;
  }
  .card {
    position: absolute;
    top: 196px;
    width: 520px;
    height: 297px;
    border-radius: 14px;
    overflow: hidden;
  }
  /* Front */
  .card-front { left: 50px; background: var(--brand-red); color: var(--paper); }
  .front-mark {
    position: absolute; left: 0; right: 0; top: 96px;
    text-align: center;
    font-size: 30px; font-weight: 700; letter-spacing: 0.5px; line-height: 1.15;
  }
  .front-url {
    position: absolute; left: 0; right: 0; bottom: 56px;
    text-align: center; font-size: 15px;
  }
  /* Back */
  .card-back { left: 630px; background: var(--paper); color: var(--ink); }
  .ghost-mark {
    position: absolute; left: 22px; top: 60px;
    font-size: 64px; font-weight: 700; line-height: 1; color: var(--ghost);
  }
  .back-mark {
    position: absolute; right: 46px; top: 34px; width: 170px;
    text-align: center; font-size: 17px; font-weight: 700; line-height: 1.2; color: var(--ink);
  }
  .top-rule {
    position: absolute; left: 30px; right: 30px; top: 128px;
    border-top: 1px solid var(--rule);
  }
  .social {
    position: absolute; right: 30px; top: 140px; text-align: right;
  }
  .social-dots { display: flex; justify-content: flex-end; gap: 6px; margin-bottom: 6px; }
  .social-dot { width: 16px; height: 16px; border-radius: 50%; background: var(--brand-red); }
  .social-handle { font-size: 13px; color: #444; }
  .person { position: absolute; left: 30px; top: 166px; }
  .person-name { font-size: 24px; font-weight: 700; color: var(--brand-red); }
  .person-title { font-size: 13px; color: var(--muted); margin-top: 2px; }
  .person-rule {
    position: absolute; left: 30px; right: 30px; top: 214px;
    border-top: 1px solid var(--rule);
  }
  .contact { position: absolute; left: 30px; top: 222px; font-size: 14px; color: #333; }
  .contact-line { display: flex; align-items: center; gap: 8px; height: 18px; }
  .contact-line svg { width: 12px; height: 12px; fill: var(--brand-red); flex: none; }
  .bottom-band { position: absolute; left: 0; bottom: 0; width: 520px; height: 46px; }
  .band-url {
    position: absolute; right: 26px; bottom: 19px;
    font-size: 14px; color: var(--paper);
  }
</style>
</head>
<body>

<section class="card card-front" aria-label="Business card front">
  <div class="front-mark">Northland's<br>Blue Wagon</div>
  <div class="front-url">www.northlandsbluewagon.net</div>
</section>

<section class="card card-back" aria-label="Business card back">
  <div class="ghost-mark" aria-hidden="true">Northland's<br>Blue Wagon</div>

  <div class="back-mark">Northland's<br>Blue Wagon</div>
  <div class="top-rule"></div>

  <div class="social">
    <div class="social-dots">
      <span class="social-dot"></span>
      <span class="social-dot"></span>
    </div>
    <div class="social-handle">northlandsbluewagon</div>
  </div>

  <div class="person">
    <div class="person-name">Ethan Marlow</div>
    <div class="person-title">President</div>
  </div>
  <div class="person-rule"></div>

  <div class="contact">
    <div class="contact-line">
      <svg viewBox="0 0 24 24" aria-hidden="true"><path d="M6.6 10.8a15 15 0 0 0 6.6 6.6l2.2-2.2a1 1 0 0 1 1-.25 11.4 11.4 0 0 0 3.6.57 1 1 0 0 1 1 1V20a1 1 0 0 1-1 1A17 17 0 0 1 3 4a1 1 0 0 1 1-1h3.5a1 1 0 0 1 1 1c0 1.25.2 2.45.57 3.57a1 1 0 0 1-.25 1z"/></svg>
      <span>628-947-2071</span>
    </div>
    <div class="contact-line">
      <svg viewBox="0 0 24 24" aria-hidden="true"><path d="M2 5h20v14H2z M2 5l10 8 10-8" fill="none" stroke="#d10000" stroke-width="2.4"/></svg>
      <span>Oakridge@northlandsbluewagon.net</span>
    </div>
  </div>

  <svg class="bottom-band" viewBox="0 0 520 46" aria-hidden="true">
    <path d="M300 0 H520 V34 H0 V30 H292 Z" fill="#d10000"/>
    <rect x="0" y="36" width="520" height="4" fill="#1a1a1a"/>
    <rect x="0" y="42" width="520" height="4" fill="#d10000"/>
  </svg>
  <div class="band-url">www.northlandsbluewagon.net</div>
</section>

</body>
</html>
```